TalvenInsight card back

Our company already has a logo and we have business cards. (I have included a picture of my business card front that i plan to use.) I want to promote a new division of Talven, called "TalvenInsight" and would like the back side of my card designed to promote this division using the same color scheme and concept as front. So I'm looking for a design for the TalvenInsight (back) side of my card. This back side does need any contact info - including that it doesn't need my name, phone, email etc. I have included the tag line that I would like to have included on that TalvenInsight side of the card. But i'd like the design to reflect "wisdom" but using a similar theme as in our sun logo. One concept i have for this side of the card has the sun is entirely out of the box and lighting up a spacious blue background to the card. Then there's a "TalvenInsight" as well as the tag line. I welcome concepts along these lines or others that you may have. Thanks!

Target Market(s)

High-end energy, or technology firms. Business leaders within the firm.

Industry/Entity Type

Professional Service

Contact Information for Business Card

The card will be double sided, but i only the need the single TalvenInsight side designed. It has to coordinate with the front side (I've included a picture of it) in color, etc.

Logo Text

TalvenInsight

Font styles to use
Other font styles liked:
• font from existing card front

Requirements
Must have
• The tie in with the Talven sun from our logo. A sense of spaciousness and/or clarity that comes from enlightened wisdom. A professional feel but a feel good feel too. The division label "TalvenInsight" and in a similar font as the existing business card. The tag line.
Should not have
• The back, TalvenINsight, side should not have contact info and should not repeat any of the front side info, given that it will be printed on the back side of card.

```html
<!DOCTYPE html>
<html lang="en">
<head>
<meta charset="utf-8">
<title>TalvenInsight card back</title>
<link href="https://fonts.googleapis.com/css2?family=Roboto:wght@400;500;700&family=Arimo:wght@400;700&display=swap" rel="stylesheet">
<style>
  :root {
    --backdrop: #e4e4e4;
    --navy: #163a6c;
    --navy-soft: #1d4578;
    --ink-navy: #17325f;
    --white: #ffffff;
    --paper: #f4f4f3;
    --sun-faint: #f6e7bb;
    --orange: #e07a1c;
    --grey-text: #9a9a9a;
    --dark-text: #3a3a3a;
  }
  * { margin: 0; padding: 0; box-sizing: border-box; }
  html, body {
    width: 1200px; height: 576px; overflow: hidden;
    background: var(--backdrop);
    font-family: "Roboto", Arial, sans-serif;
  }
  .stage { position: relative; width: 1200px; height: 576px; }

  .card {
    position: absolute; top: 139px;
    width: 484px; height: 291px;
    border-radius: 11px; overflow: hidden;
    box-shadow: 0 3px 6px rgba(0,0,0,.18);
  }

  /* Division side */
  .card--division { left: 82px; background: var(--navy); }
  .division__glow {
    position: absolute; left: 306px; top: 13px;
    width: 248px; height: 248px; border-radius: 50%;
    background: var(--navy-soft);
  }
  .division__band {
    position: absolute; left: 0; top: 51px;
    width: 264px; height: 79px; background: var(--white);
    display: flex; align-items: center; gap: 12px; padding-left: 26px;
  }
  .division__mark { width: 34px; height: 34px; background: var(--navy); flex: none; }
  .division__name {
    font-family: "Roboto", Arial, sans-serif; font-weight: 500;
    font-size: 25px; color: var(--ink-navy); letter-spacing: .2px;
  }
  .division__tagline {
    position: absolute; left: 226px; top: 225px;
    color: var(--white); font-size: 10.5px; line-height: 13.5px;
  }
  .division__tagline strong { font-weight: 700; }

  /* Company side */
  .card--company {
    left: 602px;
    background: linear-gradient(100deg, var(--paper), var(--white) 70%);
  }
  .company__glow {
    position: absolute; left: -6px; top: 2px;
    width: 208px; height: 208px; border-radius: 50%;
    background: var(--sun-faint);
  }
  .definition {
    position: absolute; left: 19px; top: 51px; width: 200px;
    font-family: "Arimo", Arial, sans-serif; font-size: 12px; line-height: 15.5px;
    color: var(--dark-text);
  }
  .definition__term { font-weight: 700; color: #222; }
  .definition__origin { font-style: italic; color: var(--grey-text); }
  .definition__muted { color: var(--grey-text); }

  .company__brand {
    position: absolute; right: 33px; top: 46px;
    display: flex; align-items: center; gap: 8px;
  }
  .company__mark { width: 30px; height: 30px; background: var(--navy); }
  .company__name {
    font-family: "Roboto", Arial, sans-serif; font-weight: 500;
    font-size: 25px; color: var(--ink-navy);
  }

  .contact {
    position: absolute; right: 31px; top: 133px; text-align: right;
    color: var(--ink-navy);
  }
  .contact__person { font-size: 16.5px; font-weight: 700; line-height: 20px; }
  .contact__role { font-size: 12px; line-height: 16px; margin-bottom: 14px; }
  .contact__line { font-size: 11.5px; line-height: 15.8px; }
  .contact__web { color: var(--orange); }
</style>
</head>
<body>
<main class="stage">
  <section class="card card--division" aria-label="TalvenInsight card side">
    <div class="division__glow"></div>
    <div class="division__band">
      <span class="division__mark"></span>
      <span class="division__name">TalvenInsight</span>
    </div>
    <p class="division__tagline">
      <strong>Talven + Insight = TalvenInsight</strong><br>
      Offering Vision, Creativity and Resilience to<br>
      Individuals and Organizations
    </p>
  </section>

  <section class="card card--company" aria-label="Talven card side">
    <div class="company__glow"></div>
    <p class="definition">
      <span class="definition__term">talven</span>
      <span class="definition__origin">&lt;Latin: to reveal&gt;</span><br>
      <span class="definition__muted">1. To unlock, unclose;<br>to lay open;</span>
      2. To bring, clarity, focus, purpose, and leadership to critical electric industry matters
    </p>
    <div class="company__brand">
      <span class="company__mark"></span>
      <span class="company__name">Talven</span>
    </div>
    <div class="contact">
      <p class="contact__person">Mara Quillen</p>
      <p class="contact__role">President</p>
      <p class="contact__line">4170 Linden Crest Way</p>
      <p class="contact__line">Alder Bay, CA 95012</p>
      <p class="contact__line">O: 555-214-3807 | M: 555-214-6650</p>
      <p class="contact__line">F: 555-214-3890 | mquillen@talven.co</p>
      <p class="contact__line contact__web">www.talven.example</p>
    </div>
  </section>
</main>
</body>
</html>
```